Rollup Display Poster Design Layout

We need 4 roll-up banner designs, 1 for each division of our company: (See required specification sheet attached)
-Divisions:
1- Electrical Contracting (yellow)
2- Security & Access Control (red)
3- Telecommunication Cabling (green)
4- Building Automation & Controls (blue)
See attached logos, there are 4 logos in total, one representing each division of our company by "Color"; see notation above to the right of each division name.
Each banner is to have 4 pictures laid out vertically stacked one on-top of each other filling up the full length of the banner which has a high of 97"
The file names for the various pictures which include the division name followed by a number (1 thur 4) indicating the preferable order in which they should be placed. However feel free to use your judgement to rearrange them.
The division name and # with be followed by a - and a "phase" such as "Generators". This second word following the division name should be superimposed on its respective picture on the banner.
The division's logo should be layout along top of the banner and taking up the full width which is 33" minus the margin.
Thank you for your consideration on this project!
Target Market(s)
Property Management, Property Owners
Industry/Entity Type
Electrical
Colors
Designer to choose colors to be used in the design.
Look and feel
Each slider illustrates characteristics of the customer's brand and the style your logo design should communicate.

```html
<!DOCTYPE html>
<html lang="en">
<head>
<meta charset="utf-8">
<title>Vale Electric LLC – Security &amp; Access Control Roll-up</title>
<link rel="stylesheet" href="https://fonts.googleapis.com/css2?family=Roboto+Condensed:wght@400;700&display=swap">
<style>
  :root {
    --red: #d0202a;
    --black: #231f20;
    --white: #ffffff;
    --stage: #e4e4e4;
    --ink: #1c1c1c;
  }
  html, body {
    margin: 0;
    width: 1200px;
    height: 1200px;
    overflow: hidden;
    background: var(--stage);
  }
  .rollup {
    position: absolute;
    left: 385px;
    top: 29px;
    width: 430px;
    height: 1142px;
    background: var(--white);
    box-shadow: 0 2px 10px rgba(0,0,0,0.15);
  }
  .rollup svg { display: block; width: 100%; height: 100%; }
  .brand-name { font-family: "Roboto Condensed", sans-serif; font-weight: 700; fill: var(--red); }
  .brand-tag { font-family: "Roboto Condensed", sans-serif; font-weight: 700; fill: var(--black); letter-spacing: 1.4px; }
  .strip-label { font-family: "Roboto Condensed", sans-serif; font-weight: 700; fill: var(--white); }
  .photo-label { font-family: "Roboto Condensed", sans-serif; font-weight: 700; fill: var(--ink); }
  .headline { font-family: "Roboto Condensed", sans-serif; font-weight: 700; fill: var(--ink); }
  .contact { font-family: "Roboto Condensed", sans-serif; font-weight: 700; fill: var(--ink); }
  .band-red { fill: var(--red); }
  .band-black { fill: var(--black); }
</style>
</head>
<body>
<div class="rollup">
  <svg viewBox="0 0 485 1288" xmlns="http://www.w3.org/2000/svg">
    <defs>
      <linearGradient id="tone-cameras" x1="0" y1="0" x2="1" y2="1">
        <stop offset="0" stop-color="#e6e3df"/>
        <stop offset="1" stop-color="#bdb8b2"/>
      </linearGradient>
      <linearGradient id="tone-cctv" x1="0" y1="0" x2="1" y2="0">
        <stop offset="0" stop-color="#3a4a63"/>
        <stop offset="0.65" stop-color="#5d7290"/>
        <stop offset="1" stop-color="#dcdfe2"/>
      </linearGradient>
      <linearGradient id="tone-access" x1="0" y1="0" x2="1" y2="0">
        <stop offset="0" stop-color="#b9bcc2"/>
        <stop offset="0.5" stop-color="#c99a62"/>
        <stop offset="1" stop-color="#d3a76f"/>
      </linearGradient>
      <linearGradient id="tone-intercom" x1="0" y1="0" x2="1" y2="1">
        <stop offset="0" stop-color="#9aa3a6"/>
        <stop offset="1" stop-color="#4f6b3f"/>
      </linearGradient>
    </defs>

    <!-- Header -->
    <g class="brand">
      <rect x="60" y="33" width="26" height="26" class="band-red"/>
      <text class="brand-name" x="100" y="58" font-size="31">VALE ELECTRIC LLC</text>
      <text class="brand-tag" x="101" y="70" font-size="9.5">FIRE, SECURITY, &amp; ACCESS CONTROL</text>
    </g>

    <!-- Photo panels -->
    <polygon role="img" aria-label="Photo of wall-mounted security cameras"
      points="0,128 272,196 0,362" fill="url(#tone-cameras)"/>
    <polygon role="img" aria-label="Photo of a CCTV monitoring room with a wall of screens and an operator"
      points="0,362 485,112 485,430 390,478 0,565" fill="url(#tone-cctv)"/>
    <polygon role="img" aria-label="Photo of a hand presenting a key card to an electronic door lock"
      points="0,565 390,478 485,455 485,835 0,750" fill="url(#tone-access)"/>
    <polygon role="img" aria-label="Photo of an outdoor intercom keypad beside a gate"
      points="0,750 395,842 0,1005" fill="url(#tone-intercom)"/>

    <!-- Security cameras strip -->
    <polygon class="band-red" points="0,120 272,186 262,212 0,146"/>
    <text class="strip-label" font-size="21" transform="translate(40,146) rotate(13.6)">SECURITY CAMERAS</text>

    <!-- Main diagonal band -->
    <polygon class="band-red" points="272,212 485,100 485,120 282,226"/>
    <polygon class="band-black" points="242,258 485,130 485,150 252,272"/>

    <!-- CCTV label -->
    <text class="photo-label" x="340" y="292" font-size="42">CCTV</text>

    <!-- Separator wedge between CCTV and access -->
    <polygon class="band-black" points="385,478 485,415 485,470 410,470"/>
    <polygon class="band-red" points="395,480 485,460 485,505 410,492" opacity="0.9"/>

    <!-- Access control strip -->
    <polygon class="band-red" points="0,660 250,510 238,540 0,683"/>
    <polygon class="band-black" points="0,683 200,575 190,595 0,700"/>
    <text class="strip-label" font-size="20" transform="translate(76,633) rotate(-31)">ACCESS CONTROL</text>

    <!-- Intercom strip -->
    <polygon class="band-red" points="180,760 485,828 485,848 215,790"/>
    <polygon class="band-black" points="0,728 395,832 385,855 0,755"/>
    <text class="strip-label" font-size="20" transform="translate(88,770) rotate(14.5)">INTERCOM SYSTEMS</text>

    <!-- Lower accent triangles -->
    <polygon class="band-red" points="340,883 485,830 485,998"/>
    <polygon fill="#ffffff" points="395,842 425,842 340,883"/>

    <!-- Headline -->
    <text class="headline" x="243" y="1048" font-size="62" text-anchor="middle">SECURITY</text>
    <text class="headline" x="243" y="1095" font-size="38" text-anchor="middle">&amp; ACCESS CONTROL</text>

    <!-- Contact: phone -->
    <g class="contact-phone">
      <circle cx="122" cy="1155" r="23" class="band-red"/>
      <path d="M113 1143 c2-2 5-2 6 0 l3 5 c1 2 0 3-1 4 l-2 2 c1 3 4 7 7 9 l2-2 c1-1 3-2 4-1 l5 3 c2 1 2 4 0 6 l-2 2 c-3 2-9 0-15-6 c-6-6-9-13-7-17 z" fill="var(--black)"/>
      <text class="contact" x="116" y="1215" font-size="22" text-anchor="middle">123456 4789</text>
    </g>

    <!-- Contact: web -->
    <g class="contact-web">
      <circle cx="352" cy="1155" r="23" class="band-red"/>
      <circle cx="352" cy="1155" r="14" fill="none" stroke="var(--black)" stroke-width="2"/>
      <ellipse cx="352" cy="1155" rx="6" ry="14" fill="none" stroke="var(--black)" stroke-width="1.6"/>
      <line x1="338" y1="1155" x2="366" y2="1155" stroke="var(--black)" stroke-width="1.6"/>
      <text class="contact" x="347" y="1215" font-size="22" text-anchor="middle">YOURWEBSITE.COM</text>
    </g>
  </svg>
</div>
</body>
</html>
```